professional business card design for technology company

We are a small technology consulting firm, specialising in consulting based around Cloud and Managed services. Our colour scheme is yellow, blue and white, as you can see in the logos. Although we are based in melbourne australia, due to the nature of our work, our clients can be located anywhere. We are looking for a clean, professional, positive look - similar to our company logo

Target Market(s)

small business

Industry/Entity Type

Business

Contact Information for Business Card

eye catching, designed to incorporate some level of raised printing. Must contain website address, phone number, name and job title

Requirements
Must have
• Logo (attached) - use of the same colour scheme

```html
<!DOCTYPE html>
<html lang="en">
<head>
<meta charset="utf-8">
<title>Lumora Business Card</title>
<link rel="stylesheet" href="https://fonts.googleapis.com/css2?family=Lato:wght@400;700;900&display=swap">
<style>
  :root {
    --stage: #2b2b2b;
    --card-dark: #4a4a4a;
    --card-dark-edge: #3d3d3d;
    --card-light: #ffffff;
    --card-light-shade: #ececec;
    --brand-blue: #2f8fce;
    --band-blue: #2a86b8;
    --band-grey: #5a5a5a;
    --brand-yellow: #e8c21a;
    --ink: #3d3d3d;
    --ink-soft: #222222;
    --wordmark-light: #f2f2f2;
  }
  * { box-sizing: border-box; margin: 0; padding: 0; }
  html, body { width: 1200px; height: 873px; overflow: hidden; }
  body {
    background: var(--stage);
    font-family: "Lato", Arial, sans-serif;
    position: relative;
  }
  .card {
    position: absolute;
    width: 560px;
    height: 320px;
    box-shadow: 0 14px 30px rgba(0,0,0,.45);
    overflow: hidden;
  }

  /* Back face */
  .card--back {
    left: 70px; top: 80px;
    background: linear-gradient(135deg, var(--card-dark) 0%, var(--card-dark-edge) 100%);
  }
  .card--back .brand {
    position: absolute; left: 150px; top: 82px;
    display: flex; align-items: center; gap: 14px;
  }
  .card--back .brand-dot {
    width: 34px; height: 34px; border-radius: 50%;
    background: var(--brand-blue);
  }
  .card--back .brand-name {
    font-weight: 900; font-size: 62px; color: var(--wordmark-light); letter-spacing: -1px;
  }
  .card--back .website {
    position: absolute; left: 40px; bottom: 42px;
    font-weight: 700; font-size: 17px; color: var(--brand-blue);
  }
  .card--back .divider {
    position: absolute; left: 268px; top: 210px; width: 2px; height: 72px;
    background: linear-gradient(to bottom, rgba(255,255,255,0), rgba(255,255,255,.35), rgba(255,255,255,0));
  }
  .card--back .tagline {
    position: absolute; left: 290px; top: 232px;
    font-weight: 700; font-size: 15px; color: var(--brand-yellow);
  }

  /* Front face */
  .card--front {
    left: 570px; top: 460px;
    background: linear-gradient(160deg, var(--card-light) 0%, var(--card-light-shade) 100%);
  }
  .card--front .bands { position: absolute; inset: 0; }
  .card--front .brand {
    position: absolute; left: 40px; top: 100px;
    display: flex; align-items: center; gap: 12px;
  }
  .card--front .brand-dot {
    width: 30px; height: 30px; border-radius: 50%;
    background: var(--brand-blue);
  }
  .card--front .brand-name {
    font-weight: 900; font-size: 46px; color: var(--ink); letter-spacing: -1px;
  }
  .card--front .address {
    position: absolute; left: 40px; top: 196px;
    font-weight: 700; font-size: 17px; line-height: 1.3; color: var(--brand-blue);
  }
  .card--front .divider {
    position: absolute; left: 322px; top: 22px; width: 3px; height: 196px;
    background: linear-gradient(to bottom, rgba(47,143,206,0), var(--brand-blue) 40%, rgba(47,143,206,0));
  }
  .card--front .person { position: absolute; left: 345px; top: 30px; }
  .card--front .person-name { font-weight: 900; font-size: 20px; color: var(--brand-blue); }
  .card--front .person-role { font-weight: 700; font-size: 14px; color: var(--ink-soft); }
  .card--front .contacts {
    position: absolute; left: 345px; top: 108px; list-style: none;
    font-size: 15px; font-weight: 700; color: var(--ink-soft);
  }
  .card--front .contacts li { display: flex; align-items: center; gap: 8px; height: 30px; }
  .card--front .contacts li.no-icon { padding-left: 28px; }
  .icon {
    width: 20px; height: 20px; border-radius: 50%;
    background: var(--brand-yellow);
    display: flex; align-items: center; justify-content: center;
  }
</style>
</head>
<body>

  <section class="card card--back" aria-label="Business card back">
    <div class="brand">
      <span class="brand-dot"></span>
      <span class="brand-name">Lumora</span>
    </div>
    <p class="website">www.lumora.com.au</p>
    <span class="divider"></span>
    <p class="tagline">Technology That Works For You</p>
  </section>

  <section class="card card--front" aria-label="Business card front">
    <svg class="bands" width="560" height="320" viewBox="0 0 560 320">
      <path d="M0 262 L560 262 L560 320 L0 320 Z" fill="var(--band-grey)"/>
      <path d="M348 320 C352 282 366 268 400 262 L560 262 L560 232 L420 232 C370 232 346 260 340 320 Z" fill="#ffffff"/>
      <path d="M352 320 C356 286 372 252 420 244 L560 244 L560 320 Z" fill="var(--band-blue)"/>
    </svg>
    <div class="brand">
      <span class="brand-dot"></span>
      <span class="brand-name">Lumora</span>
    </div>
    <p class="address">Level 4, 212 Ashby Street<br>Melbourne, Australia. 3000</p>
    <span class="divider"></span>
    <div class="person">
      <p class="person-name">Jonah Marsh</p>
      <p class="person-role">Managing Director</p>
    </div>
    <ul class="contacts">
      <li class="no-icon">1300 LUMORA (586 672)</li>
      <li>
        <span class="icon"><svg width="12" height="12" viewBox="0 0 12 12"><path d="M2 4 Q6 1 10 4 L9 5.5 L7.5 4.8 L7.5 4 Q6 3.5 4.5 4 L4.5 4.8 L3 5.5 Z M3 7 H9 V10 H3 Z" fill="#333"/></svg></span>
        0400 555 019
      </li>
      <li>
        <span class="icon"><svg width="12" height="12" viewBox="0 0 12 12"><rect x="3.5" y="1" width="5" height="10" rx="1" fill="none" stroke="#333" stroke-width="1.2"/></svg></span>
        jmarsh@lumora.com.au
      </li>
    </ul>
  </section>

</body>
</html>
```